Zielgruppe
Medtech Company
mTOR ins ein sehr wichtiger Wachstumsregulator in menschlichen Zellen. Wenn damit etwas nicht richtig funktioniert (wenn mTOR zu aktiv ist) wachsen Zellen zu schnell und können Tumore bilden. Velinto entwickelt neue pharmazeutische Medikamente zum bremsen des mTOR-Signalwegs. mTOR arbeitet in der Zelle in zwei Formen: 'mTOR Complex 1' und 'mTOR Complex 2'. Unsere Medikamente können 'mTOR Complex 1' und 'mTOR Complex 2' unterscheiden, und werden in der Zukunft für die Behandlung der genetischen Krankheit Tuberöse Sklerose und verschiedenen Krebsarten eingesetzt.
Aufgabenstellung
Konventionelle Medikamente hemmen die Aktivität von mTOR. Bei unserem Ansatz können wir viel gezielter entweder selektiv 'mTOR complex 1' (in grün) oder 'mTOR complex 2' (in orange) hemmen. Dadurch werde unsere Medikamente besser wirken und weniger Nebenwirkungen haben. Die Unterscheidung von 'mTOR complex 1' und 'mTOR complex 2' zieht sich durch die gesamten Folien durch. Visuell erreichen wir das durch die beiden verschiedenen Farben grün und orange. Als neutrale Farbe verwenden wir blau, und als Warnfarbe rot (die Hex-Codes sind angehängt. Schrift is Helvetica Neue.
Main Colors:
Blue 36537D
Light blue E9F4FF
Gray F0F1F2
Red (bad) F43D38
Light red FFEEEE
Programs / Application area:
mTOR complex 1
Green 45A052
Light Green EDFCEE
mTOR complex 2
Orange BCB704
Light Orange FFEEE6

```html
<!DOCTYPE html>
<html lang="en">
<head>
<meta charset="utf-8">
<title>Velinto – mTOR inhibition</title>
<link href="https://fonts.googleapis.com/css2?family=Montserrat:wght@400;500;600;700;800&display=swap" rel="stylesheet">
<style>
:root{
  --blue:#36537D;
  --blue-dark:#2f4a72;
  --light-blue:#E9F4FF;
  --gray:#F0F1F2;
  --red:#F43D38;
  --green:#45A052;
  --green-bright:#3cc05a;
  --text-blue:#4a6a96;
  --muted:#c9ccd2;
  --white:#ffffff;
}
*{margin:0;padding:0;box-sizing:border-box}
html,body{width:1200px;height:4116px;overflow:hidden}
body{font-family:'Montserrat',sans-serif;color:var(--blue);background:var(--white);position:relative}
.abs{position:absolute}
a{color:inherit;text-decoration:none}

/* header / hero */
.hero{left:0;top:0;width:1200px;height:572px;background:var(--light-blue)}
.brand{display:flex;align-items:center;gap:10px;font-size:32px;font-weight:400;color:var(--blue)}
.brand .mark{width:26px;height:26px;border-radius:50%;background:var(--blue)}
.nav{top:44px;left:526px;display:flex;gap:0;font-size:12px}
.nav a{position:absolute;white-space:nowrap}
.btn-kontakt{left:917px;top:35px;width:115px;height:37px;border-radius:6px;background:var(--blue);color:#fff;font-size:12px;display:flex;align-items:center;justify-content:center}
.lang{left:1087px;top:43px;width:22px;height:22px;border-radius:50%;background:#fff;border:1px solid #e3e3e3}
.lang-caret{left:1126px;top:46px;font-size:10px}
.hero-title{left:65px;top:204px;font-size:30px;line-height:36px;color:var(--blue)}
.hero-title b{font-weight:700;display:block}
.hero-title span{font-weight:400}
.hero-sub{left:65px;top:284px;font-size:12px}
.btn{display:flex;align-items:center;justify-content:center;border-radius:16px;font-size:12px}
.btn-solid{background:var(--blue);color:#fff}
.btn-outline{border:2px solid var(--blue);color:var(--blue)}
.molecule{left:655px;top:152px;width:410px;height:367px;border-radius:40%;background:radial-gradient(circle at 45% 45%,#2f6fd6 0%,#3d7fe0 35%,#5fb35a 60%,#e0c63a 80%,rgba(233,244,255,0) 100%)}

/* snapshot */
.h2{font-size:29px;font-weight:400}
.h2 b{font-weight:700}
.badge{height:30px;border-radius:4px;background:var(--gray)}
.snap-text{left:71px;top:844px;width:440px;font-size:12px;line-height:19px;color:#3d4b63}
.snap-text p+p{margin-top:18px}
.timeline-line{left:721px;width:3px}
.step{width:74px;height:74px;border-radius:50%;display:flex;align-items:center;justify-content:center}
.step-text{left:813px;width:330px;font-size:12px;line-height:19px}

/* band */
.band{left:0;top:1366px;width:1200px;height:179px;background:var(--blue);color:#fff;text-align:center}
.band h3{font-size:21px;font-weight:500;margin-top:33px}
.band-btn{left:511px;top:82px;width:178px;height:59px;background:#fff;border-radius:14px;color:var(--blue);font-size:12px;display:flex;align-items:center;justify-content:center}

/* diseases */
.body-figure{left:419px;top:1774px;width:364px;height:503px;border-radius:140px 140px 60px 60px;background:linear-gradient(180deg,#f9d7c6 0%,#f5c3b2 40%,#e66a5c 55%,#f7cfc0 100%)}
.label{font-size:12px;font-weight:600;white-space:nowrap}
.label.g{color:var(--green)}
.label.r{color:var(--red)}
.legend-dot{width:18px;height:18px;border-radius:50%}

/* team */
.card{width:490px;height:291px;border-radius:18px;overflow:hidden}
.card.light{background:var(--light-blue);border:3px solid #e6f0f8}
.card.dark{background:var(--blue);border:3px solid #dce8f4}
.card .col{position:absolute;right:0;top:0;width:144px;height:100%}
.card.light .col{background:var(--blue)}
.card.dark .col{background:var(--light-blue)}
.card .photo{position:absolute;right:0;bottom:0;width:200px;height:200px;background:linear-gradient(160deg,#c9a78f 0%,#8e7462 55%,#4b4f58 100%);border-radius:60% 0 0 0}
.card .bio{position:absolute;left:46px;top:30px;width:250px;font-size:12px;line-height:18.5px}
.card.light .bio{color:#6785b0}
.card.dark .bio{color:#dbe6f4}
.card .name{position:absolute;left:46px;bottom:30px;font-size:12px;line-height:15px}
.card .name b{font-weight:700;display:block}
.card.light .name{color:var(--blue)}
.card.dark .name{color:#fff}

/* newsletter & footer */
.footer{left:0;top:3715px;width:1200px;height:401px;background:var(--blue);color:#fff}
.newsletter{left:213px;top:3631px;width:775px;height:129px;background:#fff;border-radius:18px;box-shadow:0 4px 14px rgba(0,0,0,.06);text-align:center}
.newsletter h4{font-size:22px;font-weight:400;margin-top:34px}
.newsletter h4 b{font-weight:700}
.nl-input{left:207px;top:73px;width:251px;height:37px;background:var(--gray);border-radius:6px 0 0 6px;font-size:12px;color:#b6bac2;display:flex;align-items:center;padding-left:24px}
.nl-btn{left:465px;top:73px;width:102px;height:37px;background:var(--blue);color:#fff;border-radius:6px;font-size:12px;display:flex;align-items:center;justify-content:center}
.f-head{font-size:16px;font-weight:700}
.f-links{font-size:12px;line-height:24px}
.addr{left:66px;top:3873px;font-size:12px;line-height:24px}
.addr b{font-weight:700}
.social{width:17px;height:17px;border-radius:50%;background:#fff}
.rule{left:66px;top:4075px;width:1068px;height:1px;background:rgba(255,255,255,.6)}
.copy{left:0;top:4089px;width:1200px;text-align:center;font-size:9px}
</style>
</head>
<body>

<!-- Hero -->
<section class="abs hero"></section>
<div class="abs brand" style="left:66px;top:34px"><span class="mark"></span>velinto</div>
<nav class="abs" style="left:0;top:46px;font-size:12px">
  <a class="abs" style="left:526px">Home</a>
  <a class="abs" style="left:612px">Technology</a>
  <a class="abs" style="left:734px">Company</a>
  <a class="abs" style="left:844px">Team</a>
</nav>
<a class="abs btn-kontakt">Kontakt</a>
<div class="abs lang"></div>
<div class="abs lang-caret">&#8964;</div>

<h1 class="abs hero-title"><b>Unleashing the therapeutic potential</b><span>of mTOR inhibition</span></h1>
<p class="abs hero-sub">From Arlen to the world</p>
<a class="abs btn btn-solid" style="left:67px;top:334px;width:201px;height:69px">Buy</a>
<a class="abs btn btn-outline" style="left:292px;top:334px;width:201px;height:69px">Contact</a>
<div class="abs molecule" role="img" aria-label="3D protein structure of the mTOR complex in blue, green, yellow and orange"></div>

<!-- Snapshot -->
<h2 class="abs h2" style="left:67px;top:700px"><b>Velinto's</b> snapshot</h2>
<div class="abs badge" style="left:67px;top:774px;width:100px"></div>
<div class="abs badge" style="left:195px;top:774px;width:120px"></div>
<div class="abs snap-text">
  <p>Lorem ipsum dolor sit amet, consectetur adipiscing elit. Mauris vitae ligula ex. Vestibulum at diam mollis, tempus augue et, tempus tortor. In quam felis, semper et consectetur vitae, consequat sed neque.</p>
  <p>Quisque ultrices eu orci non gravida. Ut efficitur neque sed libero faucibus, pellentesque vestibulum odio varius. Nullam semper convallis dolor, eget sagittis augue accumsan eu. Donec ac sapien placerat, finibus nulla vitae, porttitor turpis.</p>
</div>
<a class="abs btn btn-solid" style="left:67px;top:1043px;width:202px;height:69px">Buy</a>

<div class="abs timeline-line" style="top:846px;height:96px;background:var(--blue)"></div>
<div class="abs timeline-line" style="top:980px;height:236px;background:#e4e6ea"></div>

<div class="abs step" style="left:685px;top:772px;background:var(--blue)">
  <svg width="34" height="34" viewBox="0 0 34 34" fill="none" stroke="#fff" stroke-width="2"><path d="M14 6l8 8-4 4-8-8z"/><path d="M6 28h22M10 28c0-6 4-10 10-10"/></svg>
</div>
<div class="abs step" style="left:685px;top:906px;background:#fff;border:3px solid var(--blue)">
  <svg width="32" height="32" viewBox="0 0 32 32" fill="none" stroke="#36537D" stroke-width="2"><rect x="8" y="6" width="14" height="20" rx="2"/><path d="M8 11h14"/><circle cx="22" cy="23" r="5"/></svg>
</div>
<div class="abs step" style="left:685px;top:1043px;background:#e9eaec">
  <svg width="34" height="34" viewBox="0 0 34 34" fill="none" stroke="#fff" stroke-width="2.5"><circle cx="17" cy="17" r="12"/><path d="M11 17l4 4 8-8"/></svg>
</div>
<div class="abs step" style="left:685px;top:1179px;background:#e9eaec">
  <svg width="34" height="34" viewBox="0 0 34 34" fill="none" stroke="#fff" stroke-width="2.5"><path d="M10 10l14 14M24 10L10 24"/></svg>
</div>

<p class="abs step-text" style="top:791px;color:var(--text-blue)">We have a unique understanding of the molecular structure and function of mTOR complexes</p>
<p class="abs step-text" style="top:925px;color:var(--blue);font-weight:700">We discover and develop novel, truly selective mTOR complex 1 and mTOR complex 2 inhibitors</p>
<p class="abs step-text" style="top:1061px;color:var(--muted)">Our lead program in Tuberous Sclerosis selectively targets mTOR complex 1 with a new mode of action</p>
<p class="abs step-text" style="top:1197px;color:var(--muted)">Selective mTOR complex 1 and mTOR complex 2 inhibitors have a wide range of opportunities</p>

<!-- Band -->
<section class="abs band">
  <h3>mTOR is a master regulator of cell growth and metabolism</h3>
  <a class="abs band-btn">Contact</a>
</section>

<!-- Diseases -->
<h2 class="abs" style="left:64px;top:1658px;font-size:27px;font-weight:700">mTOR complex 1 &amp; mTOR complex 2 Diseases</h2>
<div class="abs body-figure" role="img" aria-label="Anatomical illustration of the human torso with brain, lungs and organs"></div>

<svg class="abs" style="left:0;top:1740px" width="1200" height="480" fill="none" stroke-width="1.6" stroke-dasharray="5 4">
  <g stroke="#3cc05a">
    <path d="M560 50 C520 20,440 30,398 45"/>
    <path d="M620 160 C660 140,680 110,710 105"/>
    <path d="M510 230 C480 200,450 195,420 195"/>
    <path d="M470 283 C430 290,400 285,362 285"/>
    <path d="M480 297 C450 305,430 320,420 330"/>
    <path d="M720 330 C740 280,770 290,785 310"/>
    <path d="M490 355 C450 360,420 380,405 415"/>
  </g>
  <g stroke="#F43D38">
    <path d="M680 70 C690 40,710 25,740 22"/>
    <path d="M700 170 C740 190,760 210,800 206"/>
    <path d="M700 390 C730 420,760 420,800 408"/>
  </g>
</svg>

<span class="abs label g" style="left:216px;top:1782px;line-height:15px">Malformations of cortical<br>development (MCD)</span>
<span class="abs label r" style="left:770px;top:1750px">Glioblastoma</span>
<span class="abs label g" style="left:724px;top:1840px">Neurological symptoms</span>
<span class="abs label g" style="left:214px;top:1926px">Focal cortical dysplasia (FCD)</span>
<span class="abs label r" style="left:813px;top:1936px">Breast cancer</span>
<span class="abs label g" style="left:248px;top:2017px">Benign tumors</span>
<span class="abs label g" style="left:304px;top:2072px">Pancreatic cancer</span>
<span class="abs label g" style="left:801px;top:2054px">Hemimegalencephaly (HME)</span>
<span class="abs label g" style="left:228px;top:2163px">Advanced kidney cancer</span>
<span class="abs label r" style="left:813px;top:2142px">Bladder cancer</span>

<div class="abs legend-dot" style="left:66px;top:2339px;background:var(--green-bright)"></div>
<span class="abs label g" style="left:101px;top:2341px">mTOR complex 1-associated</span>
<div class="abs legend-dot" style="left:457px;top:2339px;background:var(--red)"></div>
<span class="abs label r" style="left:492px;top:2341px">mTOR complex 2-associated</span>

<!-- Team -->
<div class="abs" style="left:560px;top:2395px;width:640px;height:1090px;background:linear-gradient(90deg,rgba(240,241,242,0) 0%,var(--gray) 40%)"></div>
<h2 class="abs" style="left:67px;top:2458px;font-size:28px;font-weight:800">TEAM</h2>
<h2 class="abs" style="left:641px;top:2458px;font-size:28px;font-weight:800">ADVISORS</h2>

<article class="abs card light" style="left:67px;top:2538px">
  <div class="col"></div>
  <div class="photo" role="img" aria-label="Portrait photo of the CEO"></div>
  <p class="bio">Expert in the field of mTOR biology with 10 years of experience.<br>(Co-)Author of breakthrough publications of the structures of human mTOR complex 1 and mTOR complex 2 in the laboratory of Prof. Jonas Falk.<br>PhD in Structural Biology from the University of Arlen.</p>
  <p class="name"><b>Dr. Lukas Brenner</b>CEO</p>
</article>
<article class="abs card light" style="left:67px;top:2873px">
  <div class="col"></div>
  <div class="photo" role="img" aria-label="Portrait photo of the Head of Biology"></div>
  <p class="bio">Expert in the field of mTOR biology.<br>Profound knowledge on mTOR signaling acquired during his PostDoc in the laboratory of Prof. Thomas R. Keller.<br>PhD in Biochemistry from the University of Northfield.</p>
  <p class="name"><b>Dr. Milan Varga</b>Head of Biology</p>
</article>
<article class="abs card light" style="left:67px;top:3209px">
  <div class="col"></div>
  <div class="photo" role="img" aria-label="Portrait photo of the medicinal chemistry lead"></div>
  <p class="bio">Over 35 years of experience on preclinical research and medicinal chemistry in the areas of cardiovascular, metabolic, infectious, inflammatory diseases, and immuno-oncology (Halvern Pharma). Over 100 patents and publications.<br>PhD in Organic Chemistry from Technical University of Eastbrook.</p>
  <p class="name"><b>Dr. Peter Salomon</b>Medicinal Chemistry</p>
</article>

<article class="abs card dark" style="left:641px;top:2538px">
  <div class="col"></div>
  <div class="photo" role="img" aria-label="Portrait photo of an advisor"></div>
  <p class="bio">Group Leader at the University of Arlen<br>• Discovery of TOR in 1991<br>• Key opinion leader in the TOR field</p>
  <p class="name"><b>Prof. Thomas R. Keller</b></p>
</article>
<article class="abs card dark" style="left:641px;top:2873px">
  <div class="col"></div>
  <div class="photo" role="img" aria-label="Portrait photo of an advisor"></div>
  <p class="bio">Group Leader at the University of Arlen<br>• First cryo-EM structures of mTOR complexes<br>• Pioneer in mTOR structural biology</p>
  <p class="name"><b>Prof. Jonas Falk</b></p>
</article>

<!-- Footer -->
<footer class="abs footer">
  <div class="abs brand" style="left:66px;top:110px;color:#fff"><span class="mark" style="background:#fff"></span>velinto</div>
  <p class="abs addr" style="left:66px;top:158px"><b>Address:</b>&nbsp; c/o Life Science Centre,<br><span style="padding-left:65px">University of Arlen</span><br><span style="padding-left:65px">Lindenweg 12</span><br><span style="padding-left:65px">4010 Arlen</span></p>
  <div class="abs social" style="left:66px;top:266px"></div>
  <div class="abs social" style="left:97px;top:266px"></div>
  <div class="abs social" style="left:127px;top:266px"></div>

  <h5 class="abs f-head" style="left:395px;top:100px">Navigation</h5>
  <div class="abs f-links" style="left:395px;top:147px">About Us<br>Technology<br>Company<br>Team</div>
  <h5 class="abs f-head" style="left:650px;top:100px">Proprietary Information</h5>
  <div class="abs f-links" style="left:650px;top:147px">mTor Complex-1<br>mTor Complex-2<br>Lead Programs<br>Researches<br>Sponsors</div>
  <h5 class="abs f-head" style="left:1013px;top:100px">Information</h5>
  <div class="abs f-links" style="left:1013px;top:147px">Privacy Policy<br>Terms &amp; Conditions<br>Careers</div>

  <div class="abs rule" style="top:360px"></div>
  <p class="abs copy" style="top:374px">Copyright © 2021 Velinto</p>
</footer>

<section class="abs newsletter">
  <h4><b>Stay Updated,</b> subscribe to our newslettes</h4>
  <div class="abs nl-input">Email</div>
  <a class="abs nl-btn">Subscribe</a>
</section>

</body>
</html>
```